Technical audit needs a report template

As our company runs various technical audits, we also provide findings on paper, online or in Powerpoint. For this reason we need an identity pack, which includes business cards, complimentary cards, letterhead and the likes.

Who would be up to create this stationery pack for us? We hope to receive a style for these documents, that look professional and can be easily extended.
Updates

Project Deadline Extended Reason: I would like to provide the opportunity to friended designers to submit their designs too! Added Sunday, October 9, 2016

Target Market(s)

Start-ups, scale-ups and investors

Industry/Entity Type

Investment

Contact Information for Business Card

Street: Kastelenhofweg 41
Postcode: 3614KT
City: Utrecht
Country: The Netherlands
Phone: +31 304185926
Cell Phone: +31 6 57193840
email: jorien@velmoraxis.example
website: https://velmoraxis.example

Requirements
Must have
• I don't have inspiration, should just be a slick design based on the logo provided.
Nice to have
• Logo could be on the back of the card?
Should not have
• Should not use different colours then the logo, or at least fit the colour scheme.

```html
<!DOCTYPE html>
<html lang="en">
<head>
<meta charset="utf-8">
<title>Velmoraxis – Stationery Pack</title>
<link href="https://fonts.googleapis.com/css2?family=PT+Sans:ital,wght@0,400;0,700;1,400&display=swap" rel="stylesheet">
<style>
  :root {
    --blue: #1a9bc9;
    --blue-deep: #0b84b0;
    --blue-bright: #35b4dc;
    --blue-pale: #5cc6e0;
    --ink: #2b2f33;
    --label: #66696c;
    --paper: #ffffff;
    --board-light: #f2f2f2;
    --board-dark: #c4c6c8;
  }
  * { margin: 0; padding: 0; box-sizing: border-box; }
  html, body { width: 1200px; height: 1000px; overflow: hidden; }
  body {
    font-family: "PT Sans", Arial, sans-serif;
    color: var(--ink);
    background: radial-gradient(ellipse 75% 70% at 55% 45%, var(--board-light) 0%, #dedfe0 55%, var(--board-dark) 100%);
    position: relative;
  }
  .board-label {
    position: absolute;
    font-size: 27px;
    color: var(--label);
    font-weight: 400;
    letter-spacing: 0.2px;
  }
  .sheet {
    position: absolute;
    background: var(--paper);
    box-shadow: 2px 3px 6px rgba(0,0,0,0.28);
    overflow: hidden;
  }
  .sheet > svg.deco { position: absolute; left: 0; top: 0; }
  .wordmark {
    position: absolute;
    display: flex;
    align-items: center;
    gap: 6px;
    font-weight: 700;
    color: var(--ink);
    white-space: nowrap;
  }
  .wordmark .mark { background: var(--blue); flex: none; }
  .wordmark.on-blue { color: #fff; }
  .wordmark.on-blue .mark { background: #fff; }
  .address, .contacts {
    position: absolute;
    text-align: right;
    font-weight: 700;
    color: var(--ink);
  }

  /* Letterhead */
  .letterhead { left: 74px; top: 93px; width: 484px; height: 681px; }
  .letterhead .wordmark { left: 47px; top: 45px; font-size: 24px; gap: 8px; }
  .letterhead .wordmark .mark { width: 42px; height: 42px; }
  .letterhead .address { right: 46px; top: 44px; font-size: 8px; line-height: 10.5px; }
  .letter-body {
    position: absolute; left: 45px; top: 216px; width: 394px;
    font-size: 8.3px; line-height: 9.45px; text-align: justify; color: #333;
  }
  .letter-body p + p { margin-top: 9.45px; text-indent: 3px; }
  .letterhead .contacts { right: 97px; top: 635px; font-size: 8px; line-height: 10px; }

  /* Compliment slip */
  .slip { left: 612px; top: 93px; width: 486px; height: 227px; }
  .slip .wordmark { left: 37px; top: 35px; font-size: 19px; }
  .slip .wordmark .mark { width: 31px; height: 31px; }
  .slip .address { right: 43px; top: 37px; font-size: 6.5px; line-height: 8.5px; font-weight: 400; }
  .slip .contacts { right: 43px; top: 73px; font-size: 6.5px; line-height: 10px; font-weight: 400; }
  .slip .contacts .web { font-weight: 700; }
  .slip .greeting {
    position: absolute; right: 98px; top: 187px;
    font-style: italic; font-size: 18px; color: var(--ink);
  }
  .slip .base-strip { position: absolute; left: 0; bottom: 0; width: 100%; height: 6px;
    background: linear-gradient(90deg, var(--blue-bright), var(--blue)); }

  /* Business cards */
  .card { top: 810px; width: 191px; height: 125px; }
  .card-front { left: 74px; }
  .card-back { left: 275px; }
  .card-front .wordmark { left: 5px; top: 5px; font-size: 15px; gap: 4px; }
  .card-front .wordmark .mark { width: 27px; height: 27px; }
  .card-front .site { position: absolute; right: 6px; bottom: 5px; font-size: 7px; color: var(--ink); }
  .card-back .person { position: absolute; right: 7px; top: 35px; text-align: right; color: #fff; font-size: 7px; line-height: 8.8px; }
  .card-back .person .name { font-weight: 700; font-size: 8.5px; line-height: 11px; }
  .card-back .person .role { font-style: italic; font-size: 6px; }
  .card-back .person .details { margin-top: 1px; }
  .card-back .card-address { position: absolute; right: 7px; top: 96px; text-align: right; color: #fff; font-size: 6px; line-height: 7.5px; }
  .card-back .wordmark { left: 5px; top: 104px; font-size: 9px; gap: 3px; }
  .card-back .wordmark .mark { width: 14px; height: 14px; }

  /* Slides */
  .slide { box-shadow: 2px 3px 7px rgba(0,0,0,0.3); }
  .slide-one { left: 625px; top: 425px; width: 311px; height: 235px; }
  .slide-two { left: 694px; top: 577px; width: 311px; height: 231px; }
  .slide-three { left: 780px; top: 712px; width: 313px; height: 233px; }
  .slide .wordmark { font-size: 11px; gap: 3px; }
  .slide .wordmark .mark { width: 16px; height: 16px; }
  .slide-one .wordmark { left: 18px; top: 18px; }
  .slide-two .wordmark { left: 20px; top: 19px; }
  .slide-three .wordmark { left: 20px; top: 20px; }
  .slide-footer { position: absolute; left: 8px; bottom: 4px; font-size: 4.5px; color: #fff; white-space: nowrap; }
  .slide-three .footer-bar { position: absolute; left: 0; bottom: 0; width: 100%; height: 11px; background: var(--blue); }
  .slide-three .slide-footer { bottom: 3px; }
</style>
</head>
<body>

  <div class="board-label" style="left:74px; top:46px;">Letterhead</div>
  <div class="board-label" style="left:612px; top:46px;">Compliment Slip</div>
  <div class="board-label" style="left:625px; top:372px;">PowerPoint Slides</div>
  <div class="board-label" style="left:74px; top:940px;">Business Card</div>

  <!-- Letterhead -->
  <section class="sheet letterhead">
    <svg class="deco" width="484" height="681" viewBox="0 0 484 681" aria-hidden="true">
      <defs>
        <linearGradient id="lhBand" x1="0" y1="0" x2="1" y2="1">
          <stop offset="0" stop-color="#35b4dc"/>
          <stop offset="1" stop-color="#0b84b0"/>
        </linearGradient>
      </defs>
      <polygon points="0,0 30,0 80,62 48,86 0,26" fill="url(#lhBand)"/>
      <polygon points="390,681 484,543 484,597 428,681" fill="url(#lhBand)"/>
      <g fill="#fff">
        <circle cx="396" cy="643" r="3"/>
        <circle cx="396" cy="653" r="3"/>
        <circle cx="396" cy="663" r="3"/>
        <circle cx="396" cy="673" r="3"/>
      </g>
    </svg>
    <div class="wordmark"><span class="mark"></span>Velmoraxis</div>
    <div class="address">Kastelenhofweg 41<br>3614KT, Utrecht<br>The Netherlands</div>
    <div class="letter-body">
      <p>Praesent in mauris eu tortor porttitor accumsan. Mauris suscipit, ligula sit amet pharetra semper, nibh ante cursus purus, vel sagittis velit mauris vel metus. Aenean fermentum risus id tortor. Integer imperdiet lectus quis justo. Integer tempor. Vivamus ac urna vel leo pretium faucibus. Mauris elementum mauris vitae tortor. In dapibus augue non sapien. Aliquam ante. Curabitur bibendum justo non orci.</p>
      <p>Lorem ipsum dolor sit amet, consectetuer adipiscing elit. Morbi gravida libero nec velit. Morbi scelerisque luctus velit. Etiam dui sem, fermentum vitae, sagittis id, malesuada in, quam. Proin mattis lacinia justo. Vestibulum facilisis auctor urna. Aliquam in lorem sit amet leo accumsan lacinia. Integer rutrum, orci vestibulum ullamcorper ultricies, lacus quam ultricies odio, vitae placerat pede sem sit amet enim. Phasellus et lorem id felis nonummy placerat. Fusce dui leo, imperdiet in, aliquam sit amet, feugiat eu, orci. Aenean vel massa quis mauris vehicula lacinia. Quisque tincidunt scelerisque libero. Maecenas libero. Etiam dictum tincidunt diam. Donec ipsum massa, ullamcorper in, auctor et, scelerisque sed, est. Suspendisse nisl. Sed convallis magna eu sem. Cras pede libero, dapibus nec, pretium sit amet, tempor quis, urna.</p>
      <p>Maecenas ipsum velit, consectetuer eu, lobortis ut, dictum at, dui. In rutrum. Sed ac dolor sit amet purus malesuada congue. In laoreet, magna id viverra tincidunt, sem odio bibendum justo, vel imperdiet sapien wisi sed libero. Suspendisse sagittis ultrices augue. Mauris metus. Nunc dapibus tortor vel mi dapibus sollicitudin. Etiam posuere lacus quis dolor. Praesent id justo in neque elementum ultrices. Class aptent taciti sociosqu ad litora torquent per conubia nostra, per inceptos hymenaeos. In convallis. Fusce suscipit libero eget elit. Praesent vitae arcu tempor neque lacinia pretium. Morbi imperdiet, mauris ac auctor dictum, nisl ligula egestas nulla, et sollicitudin sem purus in lacus.</p>
    </div>
    <div class="contacts">+31 304 185 926<br>+31 6 57 19 38 40<br>jorien@velmoraxis.example<br>velmoraxis.example</div>
  </section>

  <!-- Compliment slip -->
  <section class="sheet slip">
    <svg class="deco" width="486" height="227" viewBox="0 0 486 227" aria-hidden="true">
      <defs>
        <linearGradient id="slipBand" x1="0" y1="0" x2="0" y2="1">
          <stop offset="0" stop-color="#0b84b0"/>
          <stop offset="1" stop-color="#35b4dc"/>
        </linearGradient>
      </defs>
      <polygon points="466,0 486,0 486,157 446,119 446,37" fill="url(#slipBand)"/>
      <g fill="#fff">
        <circle cx="453" cy="78" r="2.6"/>
        <circle cx="453" cy="87" r="2.6"/>
        <circle cx="453" cy="96" r="2.6"/>
        <circle cx="453" cy="105" r="2.6"/>
      </g>
    </svg>
    <div class="wordmark"><span class="mark"></span>Velmoraxis</div>
    <div class="address">Kastelenhofweg 41<br>3614KT, Utrecht<br>The Netherlands</div>
    <div class="contacts">+31 304 185 926<br>+31 6 57 19 38 40<br>jorien@velmoraxis.example<br><span class="web">velmoraxis.example</span></div>
    <div class="greeting">With compliments</div>
    <div class="base-strip"></div>
  </section>

  <!-- Business card front -->
  <section class="sheet card card-front">
    <svg class="deco" width="191" height="125" viewBox="0 0 191 125" aria-hidden="true">
      <defs>
        <linearGradient id="cardBg" x1="0" y1="0" x2="1" y2="1">
          <stop offset="0" stop-color="#1a9bc9"/>
          <stop offset="1" stop-color="#0b84b0"/>
        </linearGradient>
        <linearGradient id="cardV" x1="0" y1="0" x2="1" y2="0">
          <stop offset="0" stop-color="#5cc6e0"/>
          <stop offset="1" stop-color="#1a9bc9"/>
        </linearGradient>
      </defs>
      <rect width="191" height="125" fill="url(#cardBg)"/>
      <polygon points="55,40 100,95 100,125 55,80" fill="url(#cardV)" opacity="0.7"/>
      <polygon points="100,95 150,45 150,80 100,125" fill="#0a77a0" opacity="0.55"/>
      <polygon points="110,125 191,50 191,125" fill="#fff"/>
    </svg>
    <div class="wordmark on-blue"><span class="mark"></span>Velmoraxis</div>
    <div class="site">velmoraxis.example</div>
  </section>

  <!-- Business card back -->
  <section class="sheet card card-back">
    <svg class="deco" width="192" height="125" viewBox="0 0 192 125" aria-hidden="true">
      <defs>
        <linearGradient id="cardBack" x1="0" y1="0" x2="1" y2="1">
          <stop offset="0" stop-color="#0b84b0"/>
          <stop offset="1" stop-color="#35b4dc"/>
        </linearGradient>
      </defs>
      <rect width="192" height="125" fill="url(#cardBack)"/>
      <polygon points="0,0 20,0 80,125 0,125" fill="#fff"/>
      <polygon points="20,0 40,0 100,62 80,125" fill="#5cc6e0" opacity="0.45"/>
    </svg>
    <div class="person">
      <div class="name">Jorien (Surname)</div>
      <div class="role">(company role)</div>
      <div class="details">jorien@velmoraxis.example<br>+31 6 57 19 38 40<br>+31 304 185 926</div>
    </div>
    <div class="card-address">Kastelenhofweg 41<br>3614KT, Utrecht<br>The Netherlands</div>
    <div class="wordmark"><span class="mark"></span>Velmoraxis</div>
  </section>

  <!-- Slide one -->
  <section class="sheet slide slide-one">
    <svg class="deco" width="311" height="235" viewBox="0 0 311 235" aria-hidden="true">
      <defs>
        <radialGradient id="glowOne" cx="0.22" cy="0.1" r="0.75">
          <stop offset="0" stop-color="#ffffff"/>
          <stop offset="0.35" stop-color="#8fd6ec"/>
          <stop offset="1" stop-color="#1a9bc9"/>
        </radialGradient>
      </defs>
      <rect width="311" height="235" fill="url(#glowOne)"/>
      <polygon points="311,0 311,235 150,235" fill="#0b84b0" opacity="0.25"/>
      <line x1="311" y1="0" x2="140" y2="235" stroke="#bfe8f5" stroke-width="2"/>
      <polygon points="0,0 8,0 18,14 10,18 0,6" fill="#0b84b0"/>
    </svg>
    <div class="wordmark"><span class="mark"></span>Velmoraxis</div>
    <div class="slide-footer">Kastelenhofweg 41, 3614KT, Utrecht</div>
  </section>

  <!-- Slide two -->
  <section class="sheet slide slide-two">
    <svg class="deco" width="311" height="231" viewBox="0 0 311 231" aria-hidden="true">
      <defs>
        <linearGradient id="bgTwo" x1="0" y1="0" x2="1" y2="1">
          <stop offset="0" stop-color="#35b4dc"/>
          <stop offset="1" stop-color="#0b84b0"/>
        </linearGradient>
      </defs>
      <rect width="311" height="231" fill="url(#bgTwo)"/>
      <polygon points="0,0 18,0 30,20 18,34 0,12" fill="#0a6f96"/>
      <polygon points="0,120 90,231 0,231" fill="#5cc6e0" opacity="0.3"/>
      <line x1="311" y1="0" x2="160" y2="231" stroke="#9fdcef" stroke-width="1.5"/>
    </svg>
    <div class="wordmark on-blue"><span class="mark"></span>Velmoraxis</div>
    <div class="slide-footer">Kastelenhofweg 41, 3614KT, Utrecht, The Netherlands</div>
  </section>

  <!-- Slide three -->
  <section class="sheet slide slide-three">
    <svg class="deco" width="313" height="233" viewBox="0 0 313 233" aria-hidden="true">
      <defs>
        <linearGradient id="paleThree" x1="0" y1="0" x2="1" y2="0">
          <stop offset="0" stop-color="#ffffff"/>
          <stop offset="1" stop-color="#cfeef7"/>
        </linearGradient>
      </defs>
      <polygon points="0,0 12,0 30,26 20,34 0,10" fill="#0b84b0"/>
      <polygon points="0,140 82,222 0,222" fill="url(#paleThree)"/>
      <polygon points="70,222 265,0 285,0 92,222" fill="#a5dff0"/>
      <polygon points="92,222 285,0 313,0 313,222" fill="#56c1dc"/>
      <polygon points="92,222 313,118 313,222" fill="#4ab9d6"/>
    </svg>
    <div class="wordmark"><span class="mark"></span>Velmoraxis</div>
    <div class="footer-bar"></div>
    <div class="slide-footer">Kastelenhofweg 41, 3614KT, Utrecht, The Netherlands | +31 304 185 926 | +31 6 57 19 38 40 | jorien@velmoraxis.example | velmoraxis.example</div>
  </section>

</body>
</html>
```